Need Business Card for our Real Estate Business with Sales Executive's Picture

PANTONE 484 C ( RED)

PANTONE 2766 C ( BLUE

Industry/Entity Type

Real Estate

Contact Information for Business Card

Name, Mobile, email, & picture of Person
Agency Phone, address, Web address

Requirements
Must have
• Our Logo Colours, Agent Picture,

```html
<!DOCTYPE html>
<html lang="en">
<head>
<meta charset="utf-8">
<title>Noriva Realty – Business Card</title>
<link rel="stylesheet" href="https://fonts.googleapis.com/css2?family=Barlow:wght@500;600&display=swap">
<style>
  :root {
    --page: #ffffff;
    --front-navy: #0c1537;
    --back-navy: #110a45;
    --ink: #1a1050;
    --accent-red: #b5452a;
    --photo-tone: #0a0a0a;
    --white: #ffffff;
  }
  html, body {
    margin: 0;
    padding: 0;
    width: 980px;
    height: 1200px;
    overflow: hidden;
    background: var(--page);
    font-family: "Barlow", Arial, sans-serif;
  }
  .canvas {
    position: relative;
    width: 980px;
    height: 1200px;
  }
  .card {
    position: absolute;
    left: 257px;
    width: 482px;
    height: 312px;
    box-sizing: border-box;
    overflow: hidden;
  }
  .card-front {
    top: 232px;
    background: var(--front-navy);
  }
  .card-back {
    top: 676px;
    background: var(--white);
    border: 2px solid #000;
  }
  .brand-name {
    position: absolute;
    font-weight: 600;
    letter-spacing: 2px;
    white-space: nowrap;
  }
  .card-front .brand-name {
    left: 0;
    right: 0;
    top: 160px;
    text-align: center;
    font-size: 30px;
    color: var(--white);
    transform: translateY(-50%);
  }
  .card-back .brand-name {
    left: 22px;
    top: 56px;
    font-size: 22px;
    color: var(--ink);
  }
  .back-shape {
    position: absolute;
    left: -2px;
    top: -2px;
  }
  .portrait-frame {
    position: absolute;
    left: 278px;
    top: 44px;
    width: 152px;
    height: 199px;
    background: var(--white);
    box-shadow: 2px 3px 6px rgba(0,0,0,0.3);
  }
  .portrait {
    position: absolute;
    left: 9px;
    top: 28px;
    width: 135px;
    height: 162px;
    background: linear-gradient(180deg, #2a2a2a 0%, var(--photo-tone) 60%);
  }
  .agent-name {
    position: absolute;
    left: 21px;
    top: 169px;
    margin: 0;
    font-size: 18px;
    font-weight: 600;
    letter-spacing: 1px;
    color: var(--ink);
  }
  .name-rule {
    position: absolute;
    left: -2px;
    top: 193px;
    width: 171px;
    height: 2px;
    background: var(--accent-red);
  }
  .contact-list {
    position: absolute;
    left: 16px;
    top: 207px;
    margin: 0;
    padding: 0;
    list-style: none;
  }
  .contact-item {
    display: flex;
    align-items: center;
    height: 30px;
    font-size: 18px;
    font-weight: 500;
    letter-spacing: 0.5px;
    color: var(--ink);
  }
  .contact-icon {
    width: 24px;
    height: 24px;
    margin-right: 6px;
    flex: none;
  }
</style>
</head>
<body>
<main class="canvas">

  <section class="card card-front" aria-label="Card front">
    <span class="brand-name">NORIVA REALTY</span>
  </section>

  <section class="card card-back" aria-label="Card back">
    <svg class="back-shape" width="482" height="312" viewBox="0 0 482 312" aria-hidden="true">
      <polygon points="246,0 482,0 482,312 432,240 432,46 283,46" fill="var(--back-navy)"/>
    </svg>

    <span class="brand-name">NORIVA REALTY</span>

    <div class="portrait-frame">
      <div class="portrait" role="img" aria-label="Portrait photo of the sales executive"></div>
    </div>

    <h2 class="agent-name">Name Surname</h2>
    <div class="name-rule"></div>

    <ul class="contact-list">
      <li class="contact-item">
        <svg class="contact-icon" viewBox="0 0 24 24" aria-hidden="true">
          <circle cx="12" cy="12" r="12" fill="var(--ink)"/>
          <path d="M8 6.5c.6-.5 1.3-.4 1.6.2l1 1.8c.3.5.1 1-.3 1.4l-.7.6c.6 1.4 1.6 2.5 3 3.1l.6-.7c.4-.4 1-.6 1.4-.3l1.8 1c.6.3.7 1 .2 1.6l-.8.9c-.7.7-1.8.8-2.8.3-2.6-1.2-4.5-3.2-5.6-5.8-.4-1-.3-2.1.4-2.8z" fill="none" stroke="var(--white)" stroke-width="1.2"/>
        </svg>
        +0123456789
      </li>
      <li class="contact-item">
        <svg class="contact-icon" viewBox="0 0 24 24" aria-hidden="true">
          <circle cx="12" cy="12" r="12" fill="var(--ink)"/>
          <rect x="6" y="8" width="12" height="9" rx="1" fill="none" stroke="var(--white)" stroke-width="1.3"/>
          <path d="M6 8.5l6 4.5 6-4.5" fill="none" stroke="var(--white)" stroke-width="1.3"/>
        </svg>
        email@email.com
      </li>
      <li class="contact-item">
        <svg class="contact-icon" viewBox="0 0 24 24" aria-hidden="true">
          <circle cx="12" cy="12" r="12" fill="var(--ink)"/>
          <path d="M12 19s-5-5-5-8.5a5 5 0 0 1 10 0C17 14 12 19 12 19z" fill="var(--white)"/>
          <circle cx="12" cy="10.5" r="1.8" fill="var(--ink)"/>
        </svg>
        Adress Street No1, City
      </li>
    </ul>
  </section>

</main>
</body>
</html>
```